Plumvale CEO needs a Crowdsourced Graphic for a Wirelark Article

I need a simple graphic / banner for a blog post that's going to be posted on Wirelark (www.wirelark.com) - the biggest tech blog in the world.

The article will be written by Tobin Marsh (Plumvale's CEO) and the title will be "Asia's Secret Crowdsourcing Boom". The article is about the tens of thousands of people using crowdsourcing websites (like Plumvale.com, Qorvel.com and Vantrio.com) in China, India, the Philippines, Australia and other countries in the Asia Pacific region.

We'd really like to get this ASAP - so early submissions encouraged. We will try and get the winning designer linked to from the article.

Thanks to everyone that submitted!  Some great designs and hard to choose! :)

Target Market(s)

Tech saavy readers, English speakers

Industry/Entity Type

Tech

Requirements
Must have
• The graphic SHOULD:
1) Have the text "Asia's secret crowdsourcing boom" with some nice design and fonts (consider grey subtle pattern background and white drop shadow on fonts) - see attached examples
2) Have an Asian theme
3) Have the dimensions 640px wide by 240px wide
Nice to have
• The graphic COULD:
1) Have references to some or all of the countries mentioned above or use Asian characters as part of the background / motif (maybe the word "crowd" or "crowd sourcing" in different languages). In Chinese, the word for crowdsourcing is "witkey" (and there are corresponding Chinese characters: ??)
2) Emphasize the word "Asia" (using color and larger/different font)
3) Use a chart showing exponential (i.e. fast) growth - like the attached
4) Have a second line of text "5 Things You Didn't Know About Crowdsourcing in Asia"

```html
<!DOCTYPE html>
<html lang="en">
<head>
<meta charset="utf-8">
<title>Asia's Secret Crowdsourcing Boom</title>
<link rel="stylesheet" href="https://fonts.googleapis.com/css2?family=Bebas+Neue&family=Lobster&family=Oswald:wght@300;400&display=swap">
<style>
  :root {
    --paper: #ececec;
    --paper-edge: #e2e2e2;
    --ink-dark: #3c3c3c;
    --ink-mid: #5a5a5a;
    --asia-green: #1f8a3a;
    --chart-fill: #0f5b3c;
    --chart-line: #3ea846;
    --marker-ring: #ffffff;
  }
  * { margin: 0; padding: 0; box-sizing: border-box; }
  html, body { width: 1200px; height: 451px; overflow: hidden; }
  body { background: var(--paper); }
  .banner {
    position: relative;
    width: 1200px;
    height: 451px;
    overflow: hidden;
    background: radial-gradient(ellipse at 40% 40%, var(--paper) 55%, var(--paper-edge) 100%);
  }
  .headline {
    position: absolute;
    left: 56px;
    top: 36px;
    white-space: nowrap;
    line-height: 1;
  }
  .headline-asia {
    font-family: "Lobster", cursive;
    font-size: 76px;
    color: var(--asia-green);
    text-shadow: 2px 2px 0 #ffffff, -1px -1px 0 #ffffff;
    vertical-align: baseline;
  }
  .headline-rest {
    font-family: "Bebas Neue", sans-serif;
    font-size: 68px;
    letter-spacing: 1px;
    color: var(--ink-dark);
    text-shadow: 2px 2px 0 #ffffff;
    margin-left: 14px;
  }
  .subhead {
    position: absolute;
    left: 58px;
    top: 136px;
    font-family: "Bebas Neue", sans-serif;
    font-size: 34px;
    letter-spacing: 0.6px;
    color: var(--ink-mid);
    text-shadow: 1px 1px 0 #ffffff;
    white-space: nowrap;
  }
  .intro {
    position: absolute;
    left: 58px;
    top: 232px;
    width: 800px;
    font-family: "Oswald", sans-serif;
    font-weight: 300;
    font-size: 26px;
    line-height: 42px;
    color: var(--ink-mid);
    text-shadow: 1px 1px 0 #ffffff;
  }
  .growth-chart {
    position: absolute;
    left: 0;
    top: 0;
    width: 1200px;
    height: 451px;
  }
</style>
</head>
<body>
  <div class="banner">
    <svg class="growth-chart" viewBox="0 0 1200 451" aria-hidden="true">
      <polygon points="441,451 591,359 788,284 962,225 1200,113 1200,451" fill="var(--chart-fill)"/>
      <polyline points="436,454 591,359 788,284 962,225 1204,111" fill="none" stroke="var(--chart-line)" stroke-width="7" stroke-linejoin="round"/>
      <circle cx="591" cy="359" r="12" fill="var(--chart-fill)" stroke="var(--marker-ring)" stroke-width="3"/>
      <circle cx="788" cy="284" r="12" fill="var(--chart-fill)" stroke="var(--marker-ring)" stroke-width="3"/>
      <circle cx="962" cy="225" r="12" fill="var(--chart-fill)" stroke="var(--marker-ring)" stroke-width="3"/>
    </svg>

    <h1 class="headline">
      <span class="headline-asia">Asia's</span><span class="headline-rest">Secret Crowdsourcing Boom</span>
    </h1>
    <h2 class="subhead">5 Things You Didn't Know About Crowdsourcing In Asia</h2>
    <p class="intro">
      Tens Of Thousands Of People Using Crowdsourcing Websites<br>
      In China, India, The Philippines, Australia And Other<br>
      Countries In The Asia Pacific Region.
    </p>
  </div>
</body>
</html>
```